Design our branded business card!

We'd love for you to design our business card and come up with a fitting design that reflects the Brimble brand. We're a growing tech startup with big ambitions. We've included our brand guidelines (contain colour palette), logo (EPS vector in CMYK) and old designs to help you on your way.

We'd like to keep the design fairly simple:

* Name
* Phone number
* Email address
* Website (www.brimble.life)
* Twitter (@brimble)
* Address (19 Fenwick Row, Leeds, UK, LS4 9QT).

This would need to include print and cutting marks.

If you have any questions just let us know!

Target Market(s)

Businesses, Press and our customers!

Industry/Entity Type

Business

Contact Information for Business Card

* Name
* Phone number
* Email address
* Twitter (@brimble)

Font styles to use
Sans Serif

Requirements
Must have
• 1. Must have the Brimble logo included.
• 2. Must use the font 'Brandon Text' in either 'light' or 'thin' (https://www.typevaultex.com/fonts/qrnfoundry/brandon-text/)
• 3. Must use exact colours references from the brand guidelines. Colours outside of the brand guidelines will be discounted. White (transparent) backgrounds are fine.
• 4. Must contain the following information:
• * Name
• * Phone number
• * Email address
• * Website (www.brimble.life)
• * Twitter (@brimble)
• * Address (19 Fenwick Row, Leeds, UK, LS4 9QT).
Nice to have
• Must use the font 'Brandon Text' in either 'light' or 'thin' (https://www.typevaultex.com/fonts/qrnfoundry/brandon-text/)
Should not have
• Colours outside of the brand guidelines will be discounted. White (transparent) backgrounds are fine.
• Avoid creating icons or including photography.

```html
<!DOCTYPE html>
<html lang="en">
<head>
<meta charset="utf-8">
<title>Brimble business card</title>
<link href="https://fonts.googleapis.com/css2?family=Open+Sans:wght@300;400;700&display=swap" rel="stylesheet">
<style>
  :root {
    --stage: #2a2b2c;
    --card-dark-a: #2c3532;
    --card-dark-b: #48524f;
    --card-light: #ffffff;
    --card-light-shade: #eef1ee;
    --brand-green: #7cc47a;
    --line-green: #5fae5d;
    --ink: #23332d;
    --white: #ffffff;
  }
  * { margin: 0; padding: 0; box-sizing: border-box; }
  html, body { width: 1200px; height: 834px; overflow: hidden; }
  body {
    background: var(--stage);
    font-family: "Open Sans", Arial, sans-serif;
    display: flex;
    align-items: center;
    justify-content: center;
    gap: 40px;
  }
  .card {
    width: 540px;
    height: 318px;
    position: relative;
    border-radius: 3px;
    overflow: hidden;
  }
  .card--front {
    background: linear-gradient(135deg, var(--card-dark-a) 0%, var(--card-dark-b) 100%);
  }
  .card--back {
    background: linear-gradient(135deg, var(--card-light) 45%, var(--card-light-shade) 100%);
    color: var(--ink);
  }
  .brand {
    display: flex;
    align-items: center;
    gap: 14px;
    position: absolute;
  }
  .brand__dot {
    border-radius: 50%;
    background: var(--brand-green);
    flex: none;
  }
  .brand__name {
    font-weight: 300;
    line-height: 1;
    letter-spacing: 1px;
  }
  .card--front .brand { left: 150px; top: 124px; }
  .card--front .brand__dot { width: 64px; height: 64px; }
  .card--front .brand__name { font-size: 60px; color: var(--white); }

  .card--back .brand { left: 44px; top: 60px; }
  .card--back .brand__dot { width: 50px; height: 50px; }
  .card--back .brand__name { font-size: 48px; color: var(--ink); }

  .divider {
    position: absolute;
    height: 1px;
    background: var(--line-green);
  }
  .divider--main { left: 108px; top: 140px; width: 360px; }
  .divider--sub { left: 108px; top: 230px; width: 190px; }

  .person { position: absolute; left: 108px; top: 152px; }
  .person__name { font-weight: 700; font-size: 15px; }
  .person__role { font-size: 13px; color: var(--brand-green); margin-top: 1px; }
  .address { position: absolute; left: 108px; top: 206px; font-size: 12.5px; }

  .contact-list {
    position: absolute;
    list-style: none;
    font-size: 12.5px;
  }
  .contact-list li { display: flex; align-items: center; gap: 12px; height: 22px; }
  .contact-list svg { width: 13px; height: 13px; flex: none; }
  .contact-list--direct { left: 108px; top: 238px; }
  .contact-list--online { left: 330px; top: 150px; }
</style>
</head>
<body>

<section class="card card--front" aria-label="Card front">
  <div class="brand">
    <span class="brand__dot"></span>
    <span class="brand__name">brimble</span>
  </div>
</section>

<section class="card card--back" aria-label="Card back">
  <div class="brand">
    <span class="brand__dot"></span>
    <span class="brand__name">brimble</span>
  </div>

  <div class="divider divider--main"></div>

  <div class="person">
    <p class="person__name">Owen Hartley</p>
    <p class="person__role">President</p>
  </div>

  <p class="address">19 Fenwick Row, Leeds, UK, LS4 9QT</p>

  <div class="divider divider--sub"></div>

  <ul class="contact-list contact-list--direct">
    <li>
      <svg viewBox="0 0 14 14" aria-hidden="true"><path d="M2 5 Q7 1 12 5 L11 7 L9 6 V5 H5 V6 L3 7 Z M3 8 H11 V12 H3 Z" fill="none" stroke="#5fae5d" stroke-width="1.3"/></svg>
      <span>+44 (0) 7700 900 318</span>
    </li>
    <li>
      <svg viewBox="0 0 14 14" aria-hidden="true"><rect x="1" y="3" width="12" height="8" fill="none" stroke="#5fae5d" stroke-width="1.3"/><path d="M1 3 L7 8 L13 3" fill="none" stroke="#5fae5d" stroke-width="1.3"/></svg>
      <span>owen@brimble.life</span>
    </li>
  </ul>

  <ul class="contact-list contact-list--online">
    <li>
      <svg viewBox="0 0 14 14" aria-hidden="true"><circle cx="7" cy="7" r="5" fill="#5fae5d"/></svg>
      <span>@brimble</span>
    </li>
    <li>
      <svg viewBox="0 0 14 14" aria-hidden="true"><circle cx="7" cy="7" r="5.5" fill="none" stroke="#5fae5d" stroke-width="1.3"/><ellipse cx="7" cy="7" rx="2.5" ry="5.5" fill="none" stroke="#5fae5d" stroke-width="1"/><path d="M1.5 7 H12.5" stroke="#5fae5d" stroke-width="1"/></svg>
      <span>www.brimble.life</span>
    </li>
  </ul>
</section>

</body>
</html>
```